Marlowick APP redesign and color change

I am looking for a new design for my app. Please see the attached current design.

Currently, I have a functioning app but the colors and design are awful!
The logo is great but the rest of the app needs a refresh.
(Logo hi res not yet available but will upload soon.)
New colors or anything that is cutting edge.

Basically: It is a secure social media app within a school system where the teachers, students and parents can text, exchange photos, plan curriculum, etc.

I NEED ONLY landing page with a new look!
Looking for one distinct design for the landing page with new look.
The developer will apply this one design towards the rest of the pages/app screens.

Because part of the social media I need the feel and look of what is now the trend. Something that will attract and keep the client(s) interested. I am really leaving all the creative work to the designer and open to any suggestions.
Updates

Target Market(s)

Schools, community, teachers, students, colleges, sport teams

Industry/Entity Type

Non Profit

Font styles to use
Serif
Sans Serif

Colors

Designer to choose colors to be used in the design.

Requirements
Must have
• Sharp, trendy, millennial feel
Nice to have
• Up to designer
Should not have
• Up to designer

```html
<!DOCTYPE html>
<html lang="en">
<head>
<meta charset="utf-8">
<title>Marlowick – Messages</title>
<link rel="stylesheet" href="https://fonts.googleapis.com/css2?family=Lato:wght@400;700&family=Roboto:wght@400&display=swap">
<style>
  :root {
    --olive: #4a5a00;
    --olive-text: #4a5200;
    --mustard: #d4a03a;
    --amber: #c8901a;
    --sand: #d9bc7e;
    --ink: #2e2e2e;
    --ink-soft: #3a3a1a;
    --card: rgba(240, 236, 222, 0.86);
    --white: #ffffff;
  }
  * { box-sizing: border-box; margin: 0; padding: 0; }
  html, body { width: 1200px; height: 2190px; overflow: hidden; background: var(--white); }
  body { position: relative; font-family: "Roboto", sans-serif; }

  .app-bar {
    position: absolute; left: 0; top: 0; width: 1200px; height: 205px;
    background: var(--olive); z-index: 3;
  }
  .app-bar__title {
    position: absolute; left: 0; right: 0; top: 100px; text-align: center;
    font-family: "Lato", sans-serif; font-weight: 700; font-size: 52px; line-height: 62px;
    color: var(--white);
  }
  .app-bar__menu { position: absolute; left: 48px; top: 110px; }
  .app-bar__add { position: absolute; left: 1096px; top: 106px; }

  .hero {
    position: absolute; left: 0; top: 205px; width: 1200px; height: 822px;
    background: linear-gradient(180deg, #a38a1c 0%, #8a8a24 35%, #9aa040 65%, #6e8a1c 100%);
  }
  .featured {
    position: absolute; left: 160px; top: 352px; width: 944px; height: 400px;
    background: var(--card);
  }
  .featured__avatar {
    position: absolute; left: 96px; top: 352px; width: 128px; height: 128px;
    background: linear-gradient(135deg, #cfc9c2, #6d6560);
    box-shadow: 6px 10px 24px rgba(0,0,0,0.25); z-index: 2;
  }
  .featured__text {
    position: absolute; left: 144px; top: 78px; width: 720px;
    font-family: "Lato", sans-serif; font-size: 46px; line-height: 73px; color: var(--olive-text);
  }
  .featured__name {
    position: absolute; left: 144px; top: 276px;
    font-size: 35px; color: var(--ink);
  }
  .featured__time {
    position: absolute; right: 80px; top: 282px;
    font-size: 29px; color: var(--amber);
  }
  .hero__dot {
    position: absolute; left: 584px; top: 694px; width: 32px; height: 32px;
    border-radius: 50%; background: var(--olive);
  }

  .search {
    position: absolute; left: 0; top: 1027px; width: 1200px; height: 192px;
    background: var(--sand); box-shadow: 0 24px 40px rgba(0,0,0,0.08);
  }
  .search__icon { position: absolute; left: 110px; top: 70px; }
  .search__label {
    position: absolute; left: 240px; top: 72px;
    font-size: 39px; line-height: 48px; color: var(--ink);
  }

  .thread { position: absolute; left: 0; width: 1200px; height: 160px; }
  .thread__avatar { position: absolute; left: 94px; top: 0; width: 128px; height: 128px; }
  .thread__avatar--group {
    background: var(--olive); color: var(--mustard);
    display: flex; align-items: center; justify-content: center; font-size: 42px;
  }
  .thread__name {
    position: absolute; left: 288px; top: 0;
    font-family: "Lato", sans-serif; font-weight: 700; font-size: 38px; line-height: 48px;
    color: var(--mustard);
  }
  .thread__time {
    position: absolute; right: 96px; top: 8px;
    font-size: 31px; line-height: 40px; color: var(--ink-soft);
  }
  .thread__preview {
    position: absolute; left: 288px; top: 76px;
    font-size: 40px; line-height: 50px; color: var(--ink);
  }
</style>
</head>
<body>
  <header class="app-bar">
    <svg class="app-bar__menu" width="62" height="44" viewBox="0 0 62 44" aria-label="Menu">
      <rect x="0" y="0" width="44" height="7" fill="#fff"/>
      <rect x="0" y="32" width="62" height="8" fill="#fff"/>
    </svg>
    <h1 class="app-bar__title">3 Messages</h1>
    <svg class="app-bar__add" width="52" height="52" viewBox="0 0 52 52" aria-label="New message">
      <rect x="22" y="0" width="8" height="52" fill="#fff"/>
      <rect x="0" y="22" width="52" height="8" fill="#fff"/>
    </svg>
  </header>

  <section class="hero" role="img" aria-label="Sunlit meadow photo of a woman in a hat lying in the grass reading a book"></section>

  <div class="featured__avatar" role="img" aria-label="Profile photo of Helena Varga"></div>
  <article class="featured">
    <p class="featured__text">Hey Oren? Let’s meet tomorrow and discuss some. . .</p>
    <p class="featured__name">Helena Varga</p>
    <p class="featured__time">5 minutes ago</p>
  </article>
  <div class="hero__dot"></div>

  <div class="search">
    <svg class="search__icon" width="54" height="54" viewBox="0 0 54 54" aria-label="Search">
      <circle cx="23" cy="23" r="17" fill="none" stroke="#4a5a00" stroke-width="9"/>
      <line x1="36" y1="36" x2="49" y2="49" stroke="#4a5a00" stroke-width="10" stroke-linecap="round"/>
    </svg>
    <span class="search__label">Search. . .</span>
  </div>

  <article class="thread" style="top:1331px">
    <div class="thread__avatar" role="img" aria-label="Profile photo of Nadia Okafor" style="background:linear-gradient(180deg,#c9b89a,#5c5a50)"></div>
    <h2 class="thread__name">Nadia Okafor</h2>
    <span class="thread__time">5 minutes ago</span>
    <p class="thread__preview">I have two tickets to the concert tonight . . .</p>
  </article>

  <article class="thread" style="top:1573px">
    <div class="thread__avatar" role="img" aria-label="Profile photo of Mira Lindqvist" style="background:linear-gradient(180deg,#8a8c80,#3a4a52)"></div>
    <h2 class="thread__name">Mira Lindqvist</h2>
    <span class="thread__time">2 days ago</span>
    <p class="thread__preview">This is amazing!</p>
  </article>

  <article class="thread" style="top:1816px">
    <div class="thread__avatar thread__avatar--group">5</div>
    <h2 class="thread__name">Jonas, Priya, Elin, Tomas . . .</h2>
    <span class="thread__time">4 days ago</span>
    <p class="thread__preview">Yeah! this looks good!</p>
  </article>

  <article class="thread" style="top:2054px">
    <div class="thread__avatar" role="img" aria-label="Profile photo of Oren Calloway" style="background:linear-gradient(180deg,#9fb0b8,#55606a)"></div>
    <h2 class="thread__name">Oren Calloway</h2>
    <span class="thread__time">1 month ago</span>
  </article>
</body>
</html>
```